Postcard Design

Hoofmere Ftness Center is a state of the art equine rehabilitation and fitness center. We offer a wide variety of options to get your equine partner in tip top performing condition. Whether is swimming in or 11 foot deep pool or exercising in the squatted, we provide a personalized program for your special horse. Some other services offered are StallAir breathing treatments, pulso drift and gallotone.
Updates
Project Deadline Extended Reason: Since the project was started we have opened for business and I have pictures using my equipment at our place of business that I would like to add to the project to be used. I have also received my logo design from one of your designers that I would like added to this project. Added Tuesday, March 15, 2016
Industry/Entity Type
Fitness
Look and feel
Each slider illustrates characteristics of the customer's brand and the style your logo design should communicate.

```html
<!DOCTYPE html>
<html lang="en">
<head>
<meta charset="utf-8">
<title>Hoofmere Ftness Center – Postcard</title>
<link rel="stylesheet" href="https://fonts.googleapis.com/css2?family=Roboto+Condensed:wght@400;700&family=Roboto:wght@400&display=swap">
<style>
  :root {
    --tan: #bcab91;
    --tan-text: #a8957a;
    --dark: #3b3b3b;
    --ink: #2f2f2f;
    --white: #ffffff;
    --page: #ececec;
    --stamp: #d9d9d9;
  }
  * { margin: 0; padding: 0; box-sizing: border-box; }
  html, body { width: 825px; height: 1200px; overflow: hidden; background: var(--page); }
  .canvas { position: relative; width: 825px; height: 1200px; }
  .card { position: absolute; left: 98px; width: 631px; height: 489px; overflow: hidden; background: var(--white); box-shadow: 0 2px 6px rgba(0,0,0,.18); }
  .card--front { top: 68px; }
  .card--back { top: 618px; background: var(--tan); }
  .shapes { position: absolute; inset: 0; }
  .cond { font-family: "Roboto Condensed", "Arial Narrow", sans-serif; }
  .nowrap { white-space: nowrap; }

  /* front */
  .pool-photo { position: absolute; left: 359px; top: 0; width: 272px; height: 267px; border-bottom-left-radius: 115px 120px; background: linear-gradient(180deg, #7d8b74 0%, #5a4438 35%, #3f8e9b 60%, #6bc3c9 100%); }
  .headline { position: absolute; left: 28px; top: 28px; font-weight: 700; font-size: 21px; line-height: 27px; color: var(--ink); white-space: nowrap; }
  .headline .accent { color: var(--tan-text); }
  .contact-pill { position: absolute; left: -4px; top: 133px; width: 320px; height: 46px; border: 3px solid var(--dark); border-radius: 0 23px 23px 0; background: var(--tan); color: var(--ink); font-size: 22px; line-height: 40px; padding-left: 44px; white-space: nowrap; }
  .avatar { position: absolute; top: 204px; width: 104px; height: 104px; border-radius: 50%; border: 6px solid var(--dark); }
  .avatar--1 { left: 20px; background: radial-gradient(circle at 50% 45%, #f2ddd3, #e6c6bb 60%, #f7eeea); }
  .avatar--2 { left: 137px; background: radial-gradient(circle at 50% 50%, #9a7260, #5a4a42 60%, #f3f1ee); }
  .avatar--3 { left: 262px; background: radial-gradient(circle at 50% 50%, #d9b59a, #c9c3a0 60%, #f4f2ee); }
  .services { position: absolute; left: 38px; top: 337px; font-weight: 700; font-size: 12.5px; color: var(--ink); white-space: nowrap; }
  .offer { position: absolute; left: 38px; top: 364px; font-size: 18.5px; line-height: 24px; letter-spacing: .4px; color: var(--white); white-space: nowrap; }
  .model-photo { position: absolute; z-index: 2; left: 450px; top: 297px; width: 166px; height: 178px; border-radius: 40% 40% 10% 10%; background: linear-gradient(180deg, #c99a84 0%, #efe6df 35%, #5c6476 65%, #b7d24a 100%); opacity: .9; }
  .visit-bar { position: absolute; z-index: 1; left: 0; top: 442px; width: 631px; height: 47px; background: var(--dark); color: var(--white); font-family: "Roboto", Arial, sans-serif; font-size: 17px; letter-spacing: 3.6px; line-height: 47px; padding-left: 50px; white-space: nowrap; }

  /* back */
  .art-panel { position: absolute; left: 0; top: 0; width: 304px; height: 207px; background: radial-gradient(ellipse at 55% 55%, #d24a7a 0%, #3c6fc9 25%, #f0b43a 45%, #1c1c1c 75%, #000 100%); }
  .contact-box { position: absolute; left: 0; top: 214px; width: 304px; height: 98px; background: var(--dark); color: var(--white); font-weight: 700; font-size: 21px; text-transform: uppercase; white-space: nowrap; display: flex; align-items: center; padding-left: 40px; }
  .back-headline { position: absolute; left: 35px; top: 346px; font-weight: 700; font-size: 16.5px; line-height: 23px; color: var(--white); white-space: nowrap; }
  .back-visit { position: absolute; left: 35px; top: 428px; font-family: "Roboto", Arial, sans-serif; font-size: 15px; color: var(--ink); white-space: nowrap; }
  .stamp-box { position: absolute; left: 526px; top: 32px; width: 72px; height: 71px; background: var(--stamp); }
</style>
</head>
<body>
<main class="canvas">

  <section class="card card--front">
    <svg class="shapes" width="631" height="489" viewBox="0 0 631 489" aria-hidden="true">
      <path d="M0,185 Q40,270 200,268 L631,268 L631,442 L0,442 Z" fill="var(--tan)"/>
      <path d="M0,195 Q45,272 200,272 L631,272" fill="none" stroke="var(--white)" stroke-width="3"/>
      <path d="M350,0 L631,0 L631,276 L470,276 Q350,276 350,150 Z" fill="var(--tan)"/>
    </svg>
    <div class="pool-photo" role="img" aria-label="Horse standing in a rehabilitation swimming pool"></div>

    <h1 class="headline cond">Hoofmere Ftness Center is a state<br><span class="accent">of the art equine rehabilitation</span><br>and fitness center</h1>
    <p class="contact-pill cond">Contact us at: 123.456.789</p>

    <div class="avatar avatar--1" role="img" aria-label="Fitness model portrait"></div>
    <div class="avatar avatar--2" role="img" aria-label="Athlete portrait"></div>
    <div class="avatar avatar--3" role="img" aria-label="Woman lifting a dumbbell"></div>

    <p class="services cond">StallAir breathing treatments, pulso drift and gallotone.</p>
    <p class="offer cond">We offer a wide variety of options to get your<br>equine partner in tip top performing condition</p>
    <div class="model-photo" role="img" aria-label="Woman in a wide squat exercise pose"></div>

    <p class="visit-bar">Visit us at www.website.com</p>
  </section>

  <section class="card card--back">
    <svg class="shapes" width="631" height="489" viewBox="0 0 631 489" aria-hidden="true">
      <path d="M306,0 L306,390 Q306,472 400,478" fill="none" stroke="var(--white)" stroke-width="3"/>
      <path d="M320,0 L631,0 L631,489 L410,489 Q320,489 320,400 Z" fill="var(--white)"/>
      <rect x="0" y="207" width="306" height="7" fill="var(--white)"/>
      <rect x="304" y="0" width="3" height="314" fill="var(--white)"/>
    </svg>
    <div class="art-panel" role="img" aria-label="Colourful illustrated horse head on black"></div>
    <p class="contact-box cond">Contact us at: 123.456.789</p>
    <h2 class="back-headline cond">Hoofmere Ftness Center is a state<br>of the art equine rehabilitation<br>and fitness center</h2>
    <p class="back-visit">Visit us at www.website.com</p>
    <div class="stamp-box" aria-hidden="true"></div>
  </section>

</main>
</body>
</html>
```